Flyer
Super tolle Arbeit, Greta hat sich wahnsinnige Mühe gegeben und ein perfektes Ergebnis geliefert. Jederzeit wieder!!!
Zielgruppe
Wir bauen hochwertige Design Esstische aus Holz auch Couchtische und Konferenztische unser Zielgruppe sind Menschen die Wert auch hochwertige Handarbeit legen und denen Design wichtig ist
Aufgabenstellung
Bitte designt einen Flyer, bei den Format bin ich offen, nur keine Spezial Formate die dann beim Drucken teurer sind. Ansonsten sollten Bilder unserer Tische zu sehen sein, außerdem ein Text mit der Beschreibung was wir machen, wofür wir stehen und was uns wichtig ist. Es sollte auch ein Bild von meinem Kollegen und mir zu sehen sein und die Kontaktdaten natürlich. Bilder und Texte könnt ihr der Website entnehmen. Wir stehen für ein minimalistisches und cleanes design und das sollte bei dem Flyer ebenfalls der Fall sein.

```html
<!DOCTYPE html>
<html lang="de">
<head>
<meta charset="utf-8">
<title>Lindqvist Manufaktur – Flyer</title>
<link rel="stylesheet" href="https://fonts.googleapis.com/css2?family=Inter:wght@300;400;500;600&display=swap">
<style>
  :root {
    --stage: #2b2724;
    --paper: #ffffff;
    --ink: #1c1c1c;
    --ink-soft: #4a4a4a;
    --band: #1e1e1e;
    --band-grey: #5c5c5c;
    --on-dark: #f2f2f2;
    --accent: #2a7fa8;
  }
  * { box-sizing: border-box; margin: 0; padding: 0; }
  html, body { width: 1139px; height: 1200px; overflow: hidden; }
  body {
    background: var(--stage);
    font-family: "Inter", sans-serif;
    color: var(--ink);
    position: relative;
  }
  .sheets {
    position: absolute;
    left: 194px; top: 51px;
    width: 987px; height: 1446px;
    transform: scale(0.76);
    transform-origin: top left;
  }
  .page {
    position: absolute; left: 0;
    width: 987px; height: 698px;
    background: var(--paper);
    overflow: hidden;
  }
  .page--front { top: 0; }
  .page--back { top: 748px; }

  /* front */
  .brand {
    position: absolute; left: 42px; top: 22px;
    width: 110px; text-align: center;
  }
  .brand__dot {
    width: 96px; height: 96px; margin: 0 auto 8px;
    border-radius: 50%; border: 4px solid var(--ink);
    background: #f6f2ea;
  }
  .brand__name {
    font-size: 10px; font-weight: 400; letter-spacing: 1.5px;
    text-transform: uppercase; color: var(--ink);
  }
  .hero {
    position: absolute; left: 153px; top: 0;
    width: 780px; height: 345px;
    background: radial-gradient(ellipse 48% 32% at 50% 45%, #d9a46a 0%, #e6bd8a 55%, #f6efe6 80%, #ffffff 100%);
  }
  .front-band {
    position: absolute; left: 0; top: 451px;
    width: 987px; height: 247px; background: var(--band);
  }
  .gallery {
    position: absolute; left: 42px;
    display: flex; gap: 16px;
  }
  .gallery--front { top: 348px; }
  .gallery--back { top: 42px; }
  .photo { width: 290px; height: 205px; }
  .gallery--back .photo { height: 334px; }
  .photo--concrete { background: linear-gradient(160deg, #6f6f6f, #a59b8d 60%, #8c8c8c); }
  .photo--lounge { background: linear-gradient(170deg, #3a3a3c 0%, #b07a4c 55%, #9c8e86 100%); }
  .photo--dining { background: linear-gradient(160deg, #cfd3d6 0%, #8f6e50 55%, #3d4f86 100%); }
  .photo--tunnel { background: radial-gradient(ellipse at 50% 30%, #cfcfcf 0%, #7a7a7a 35%, #454545 100%); }
  .photo--slab { background: radial-gradient(ellipse at 60% 60%, #e6b778 0%, #cf9b5c 50%, #5e6a7a 100%); }
  .photo--workshop { background: linear-gradient(160deg, #4a4440 0%, #232323 55%, #8b6b4e 100%); }

  .headline {
    position: absolute; left: 42px; top: 575px;
    font-size: 44px; font-weight: 300; line-height: 1.05;
    color: var(--on-dark); letter-spacing: 0.5px;
  }
  .intro {
    position: absolute; left: 425px; top: 582px; width: 500px;
    color: var(--on-dark); font-size: 12px; line-height: 1.45;
  }
  .intro__lead { font-size: 14px; font-weight: 500; margin-bottom: 14px; }
  .intro p + p { margin-top: 10px; }

  /* back */
  .columns {
    position: absolute; left: 42px; top: 394px;
    display: flex; gap: 16px;
  }
  .column { width: 290px; font-size: 12px; line-height: 1.4; color: var(--ink-soft); }
  .column h2 {
    font-size: 20px; font-weight: 400; color: var(--ink);
    line-height: 1.15; margin-bottom: 8px;
  }
  .column p + p { margin-top: 12px; }
  .column--promise { padding-left: 5px; }
  .promise-list { list-style: none; padding-left: 10px; }
  .promise-list li { position: relative; padding-left: 15px; margin-bottom: 7px; }
  .promise-list li::before {
    content: ""; position: absolute; left: 0; top: 6px;
    width: 5px; height: 5px; border-radius: 50%; background: var(--accent);
  }
  .footer {
    position: absolute; left: 0; top: 608px;
    width: 987px; height: 90px; display: flex;
  }
  .footer__cta {
    width: 493px; background: var(--band-grey); color: var(--on-dark);
    padding: 14px 42px; font-size: 12px; line-height: 1.4;
  }
  .footer__cta h3 { font-size: 20px; font-weight: 400; margin-bottom: 8px; }
  .footer__contact {
    flex: 1; background: var(--band); color: var(--on-dark);
    display: flex; padding: 18px 0 0 87px; gap: 80px;
  }
  .footer__contact h3 { font-size: 20px; font-weight: 400; }
  .contact-lines { font-size: 12px; line-height: 1.6; padding-top: 4px; }
  .contact-lines strong { font-weight: 600; }
</style>
</head>
<body>
<div class="sheets">
  <section class="page page--front">
    <div class="hero" role="img" aria-label="Produktfoto: Massivholz-Tischplatte mit Baumkante und Glasfüßen auf weißem Grund"></div>
    <div class="brand">
      <div class="brand__dot"></div>
      <div class="brand__name">Lindqvist Manufaktur</div>
    </div>
    <div class="front-band"></div>
    <div class="gallery gallery--front">
      <div class="photo photo--concrete" role="img" aria-label="Holztisch mit schwarzen Beinen in Betonraum"></div>
      <div class="photo photo--lounge" role="img" aria-label="Couchtische aus Baumscheiben vor einem Sofa"></div>
      <div class="photo photo--dining" role="img" aria-label="Esstisch aus Holz in hellem Wohnraum mit Blumen"></div>
    </div>
    <h1 class="headline">Tischunikate aus<br>einem Stück.</h1>
    <div class="intro">
      <p class="intro__lead">Willkommen bei der Lindqvist Manufaktur.</p>
      <p>Wir fertigen hochwertige Monolith-Tische aus einer einzigen Bohle heimischen Holzes.<br>Zeitlos, beständig und mit Liebe zum Detail.</p>
      <p>Ein Statement für Ihr Zuhause.</p>
    </div>
  </section>

  <section class="page page--back">
    <div class="gallery gallery--back">
      <div class="photo photo--tunnel" role="img" aria-label="Holztisch mit Glasbeinen in einem Tunnel"></div>
      <div class="photo photo--slab" role="img" aria-label="Baumscheiben-Tische mit schwarzem Harz, von oben"></div>
      <div class="photo photo--workshop" role="img" aria-label="Die beiden Gründer montieren Glasbeine in der Werkstatt"></div>
    </div>
    <div class="columns">
      <article class="column">
        <h2>Unsere Leidenschaft:<br>Einzigartigkeit.</h2>
        <p>Unsere Motivation ist es, Möbel von herausragender Handwerkskunst zu schaffen, die von Herzen kommen. Jedes Stück ist ein Unikat, gefertigt in enger Zusammenarbeit mit Ihnen. Wir verwirklichen Ihre individuelle Vorstellung und schaffen ein Möbelstück, das nicht nur funktional ist, sondern auch eine emotionale Verbindung zu Ihnen hat.</p>
      </article>
      <article class="column column--promise">
        <h2>Unser Versprechen:</h2>
        <ul class="promise-list">
          <li>Hochwertigste Verarbeitung aus massivem, heimischem Holz</li>
          <li>Jeder Tisch ein Unikat aus einem Stück</li>
          <li>Minimalistisches, zeitloses Design</li>
          <li>Individuelle Konfiguration nach Ihren Wünschen</li>
          <li>Persönliche Beratung und enge Zusammenarbeit</li>
        </ul>
      </article>
      <article class="column">
        <h2>Handwerk &amp; Persönlichkeit</h2>
        <p>Hinter der Lindqvist Manufaktur stehen Jonas Lindqvist und Felix Amrein. In unserer Werkstatt in Stuttgart fertigen wir Esstische, Couchtische, Waschtischplatten und Konferenztische aus Holzmonolithen – jedes Stück individuell, jedes Stück mit eigener Geschichte</p>
        <p>Wir kennen den Ursprung des Holzes, den Standort des Baumes und seine Geschichte. So entsteht mehr als ein Möbelstück: ein echtes Erlebnis.</p>
      </article>
    </div>
    <footer class="footer">
      <div class="footer__cta">
        <h3>Ihr Tisch. Ihr Unikat.</h3>
        <p>Konfigurieren Sie Ihren persönlichen Traumtisch oder lassen Sie sich von unseren Arbeiten inspirieren.</p>
      </div>
      <div class="footer__contact">
        <h3>Kontakt</h3>
        <div class="contact-lines">
          <strong>Lindqvist Manufaktur</strong><br>
          www.lindqvist-manufaktur.de<br>
          Instagram: @lindqvist_manufaktur
        </div>
      </div>
    </footer>
  </section>
</div>
</body>
</html>
```